Chiropractic Flyers to be made more up to date

I have used this series of flyers for my own practice. I would like the graphics to be brought up to date and the name of the doctor and the practice, the address, phone number and date to be removed and a blank box inserted in one place on the flyer that other chiropractors could use to personalize the flyers for their practice. On some of the flyers, this information is in several places. I'd like to have it all in one space so that it would be easy for the doctor to add it in their practice. They all need to be bright and colorful with catchy graphics.

Industry/Entity Type

Doctor

```html
<!DOCTYPE html>
<html lang="en">
<head>
<meta charset="utf-8">
<title>Get Your Back On Track – Chiropractic Flyer</title>
<link rel="stylesheet" href="https://fonts.googleapis.com/css2?family=Bebas+Neue&family=Didact+Gothic&family=Josefin+Sans:wght@300;400&display=swap">
<style>
  :root {
    --page-bg: #e8e8ee;
    --ink-dark: #262f3b;
    --mint: #86cc9c;
    --mint-text: #7fcf9f;
    --pink: #e8336e;
    --ocean: #057a94;
    --teal: #2f7e69;
    --heading-ink: #232a36;
    --white: #ffffff;
    --footer-grey: #8a97a3;
  }
  * { margin: 0; padding: 0; box-sizing: border-box; }
  html, body { width: 1040px; height: 1200px; overflow: hidden; background: var(--page-bg); }
  .flyer {
    position: absolute; left: 131px; top: 54px;
    width: 778px; height: 1092px;
    display: flex; flex-direction: column;
    box-shadow: 0 12px 30px rgba(0,0,0,.25);
  }
  .top-strip { height: 17px; background: var(--ink-dark); }
  .title-band {
    height: 134px; background: var(--mint);
    display: flex; align-items: center; justify-content: center;
  }
  .title-band h1 {
    font-family: "Bebas Neue", sans-serif; font-weight: 400;
    font-size: 80px; color: var(--pink); letter-spacing: 0.5px; line-height: 1;
    padding-top: 6px;
  }
  .benefits {
    height: 266px; background: var(--ocean);
    list-style: none; padding: 34px 70px 0 76px;
  }
  .benefits li {
    position: relative; font-family: "Didact Gothic", sans-serif;
    font-size: 23px; line-height: 28px; letter-spacing: 1.3px; color: var(--heading-ink);
    margin-bottom: 31px;
  }
  .benefits li svg { position: absolute; left: -30px; top: 6px; }
  .topics {
    height: 451px; background: var(--teal);
    display: grid; grid-template-columns: 393px 1fr; grid-template-rows: 202px 1fr;
    padding: 36px 40px 0 45px;
  }
  .topic h2 {
    font-family: "Bebas Neue", sans-serif; font-weight: 400;
    font-size: 36px; color: var(--heading-ink); line-height: 1; margin-bottom: 10px;
  }
  .topic p {
    font-family: "Josefin Sans", sans-serif; font-weight: 300;
    font-size: 14.6px; line-height: 24px; letter-spacing: -0.2px; color: var(--white); width: 330px;
  }
  .contact-band {
    position: relative; height: 154px; background: var(--ink-dark);
    font-family: "Didact Gothic", sans-serif; text-align: right; padding: 24px 4px 0 0;
  }
  .doctor-name {
    font-size: 36px; color: var(--mint-text); letter-spacing: 4px;
    font-variant: small-caps; line-height: 42px; padding-right: 24px;
  }
  .contact-line { font-size: 25px; color: var(--footer-grey); letter-spacing: 5.2px; line-height: 33px; }
  .contact-line.primary { padding-right: 62px; }
  .duty-badge {
    position: absolute; left: 2px; top: -31px;
    width: 166px; height: 166px; border-radius: 50%;
    background: var(--pink); border: 6px solid var(--ink-dark);
  }
  .bottom-band {
    flex: 1; background: var(--mint);
    display: flex; align-items: center; justify-content: space-between; padding: 0 30px 0 30px;
  }
  .profession-mark { width: 54px; height: 54px; border-radius: 4px;
    background: linear-gradient(#f3f6f4, #cfdcd5); }
  .icon-row { display: flex; gap: 21px; }
  .icon-row svg { display: block; }
</style>
</head>
<body>
<article class="flyer">
  <div class="top-strip"></div>

  <header class="title-band">
    <h1>Get Your Back On Track!</h1>
  </header>

  <ul class="benefits">
    <li><svg width="20" height="16" viewBox="0 0 20 16"><path d="M2 8 L7 13 L18 2" fill="none" stroke="#e8336e" stroke-width="4" stroke-linecap="round"/></svg>Learn how your posture can effect your attitude and self‑esteem</li>
    <li><svg width="20" height="16" viewBox="0 0 20 16"><path d="M2 8 L7 13 L18 2" fill="none" stroke="#e8336e" stroke-width="4" stroke-linecap="round"/></svg>Learn the posture of a “Winner” &amp; how to avoid the posture of a “Loser”</li>
    <li><svg width="20" height="16" viewBox="0 0 20 16"><path d="M2 8 L7 13 L18 2" fill="none" stroke="#e8336e" stroke-width="4" stroke-linecap="round"/></svg>Learn proper backpack safety to stand up for success</li>
  </ul>

  <section class="topics">
    <div class="topic">
      <h2>Back Pain</h2>
      <p>Back pain is the second most common reason for visits to the GP’s office, outnumbered by upper-respiratory infections. It is estimated that back pain affects more than half of the adult population each year.</p>
    </div>
    <div class="topic">
      <h2>Headaches</h2>
      <p>Back pain is the second most common reason for visits to the GP’s office, outnumbered by upper-respiratory infections. It is estimated that back pain affects more than half of the adult population each year.</p>
    </div>
    <div class="topic">
      <h2>Stress</h2>
      <p>Back pain is the second most common reason for visits to the GP’s office, outnumbered by upper-respiratory infections. It is estimated that back pain affects more than half of the adult population each year.</p>
    </div>
    <div class="topic">
      <h2>Headaches</h2>
      <p>Back pain is the second most common reason for visits to the GP’s office, outnumbered by upper-respiratory infections. It is estimated that back pain affects more than half of the adult population each year.</p>
    </div>
  </section>

  <footer class="contact-band">
    <div class="duty-badge" role="img" aria-label="Round chiropractor on duty badge"></div>
    <div class="doctor-name">Dr. Firstname Lastname</div>
    <div class="contact-line primary">Date, Address, Hours</div>
    <div class="contact-line">Telephon and/or email@address.com</div>
  </footer>

  <div class="bottom-band">
    <div class="profession-mark" role="img" aria-label="Chiropractic profession emblem"></div>
    <div class="icon-row">
      <svg width="42" height="42" viewBox="0 0 42 42" aria-label="Wellness"><circle cx="21" cy="21" r="21" fill="#057a94"/><circle cx="21" cy="21" r="6" fill="#fff"/><g stroke="#fff" stroke-width="2.5" stroke-linecap="round"><path d="M21 7v5M21 30v5M7 21h5M30 21h5M11 11l3.5 3.5M27.5 27.5L31 31M31 11l-3.5 3.5M14.5 27.5L11 31"/></g></svg>
      <svg width="42" height="42" viewBox="0 0 42 42" aria-label="Care"><circle cx="21" cy="21" r="21" fill="#057a94"/><path d="M21 31 C10 23 10 14 16 13 C19 12.5 21 15 21 16 C21 15 23 12.5 26 13 C32 14 32 23 21 31Z" fill="#fff"/></svg>
      <svg width="42" height="42" viewBox="0 0 42 42" aria-label="Freedom"><circle cx="21" cy="21" r="21" fill="#057a94"/><circle cx="21" cy="21" r="8" fill="#fff"/></svg>
      <svg width="42" height="42" viewBox="0 0 42 42" aria-label="Balance"><circle cx="21" cy="21" r="21" fill="#057a94"/><circle cx="21" cy="21" r="11" fill="none" stroke="#fff" stroke-width="2.5"/></svg>
    </div>
  </div>
</article>
</body>
</html>
```